Apparel store needs a cover for their seasonal catalogue

Every season the store creates a catalogue with a preview of the collection for the customers, the catalogue is printed and sent to 25 000 customers.We need a cover and back cover project for the upcoming winter season.Here is the current summer catalogue - https://www.le-carrouselo.com/catalogue.shtmlFormat165mmx240mmAttached is some older issues, please note that the name LE CARROUSEL MIRANDE should be written on it as well as automne - hiver 2019 (fall-winter 19).

Target Market(s)

medium to high price consumers - male and female

Industry/Entity Type

Shoe Store

Colors

Designer to choose colors to be used in the design.

Requirements
Must have
• company name - LE CARROUSEL MIRANDE
• season - automne hiver 2019
• "Arty feel" to it
Nice to have
• Creative ideas - abstract themes
• As exemple I uploaded some older cover, but you do not have to follow the same patterns
Should not have
• product images

```html
<!DOCTYPE html>
<html lang="fr">
<head>
<meta charset="utf-8">
<title>Le Carrousel Mirande — catalogue automne-hiver 2019</title>
<link rel="stylesheet" href="https://fonts.googleapis.com/css2?family=Montserrat:wght@300;400&family=Sacramento&display=swap">
<style>
  :root{
    --backdrop:#c8c6c7; --paper:#ffffff; --ink:#1d1d1b;
    --mint:#cfe7e0; --cream:#f2e3b1; --lilac:#c2acd3; --sage:#b5d9bf;
    --lemon:#f1ec8a; --red:#cb2f2a; --olive:#a4a438; --slate:#77949a;
    --pine:#3d7e79; --sun:#f9d05b; --peach:#f8c8b6; --clay:#dd8a69;
    --periwinkle:#d4daef; --pistachio:#cfe098; --wheat:#dac27b; --gold:#f2d66c;
    --fern:#9fad6b; --caramel:#c3a865; --coral:#f28b6c;
  }
  html,body{margin:0;padding:0;width:1200px;height:732px;overflow:hidden;background:var(--backdrop);}
  .spread{display:block;width:1200px;height:732px;}
  .page{fill:var(--paper);}
  .colour-field-front{fill:url(#front-field);}
  .colour-field-back{fill:url(#back-field);}
  .title-panel-box{fill:var(--paper);}
  .script{font-family:'Sacramento',cursive;font-size:44px;fill:var(--ink);}
  .season-title{font-family:'Montserrat',sans-serif;font-weight:400;font-size:38px;letter-spacing:5px;fill:var(--ink);}
  .tagline{font-family:'Montserrat',sans-serif;font-weight:400;font-size:19px;letter-spacing:9px;fill:var(--ink);}
  .website{font-family:'Montserrat',sans-serif;font-weight:400;font-size:36px;letter-spacing:5px;fill:var(--paper);}
  .brand-name{font-family:'Montserrat',sans-serif;font-weight:400;font-size:17px;letter-spacing:1.5px;fill:var(--ink);}
  .brand-dot{fill:var(--ink);}
</style>
</head>
<body>
<svg class="spread" viewBox="0 0 2464 1502" preserveAspectRatio="none" xmlns="http://www.w3.org/2000/svg">
  <defs>
    <linearGradient id="front-field" x1="0" y1="0" x2="0.35" y2="1">
      <stop offset="0" stop-color="var(--mint)"/>
      <stop offset="0.12" stop-color="var(--coral)"/>
      <stop offset="0.24" stop-color="var(--fern)"/>
      <stop offset="0.36" stop-color="var(--mint)"/>
      <stop offset="0.5" stop-color="var(--periwinkle)"/>
      <stop offset="0.62" stop-color="var(--pistachio)"/>
      <stop offset="0.74" stop-color="var(--gold)"/>
      <stop offset="0.86" stop-color="var(--caramel)"/>
      <stop offset="1" stop-color="var(--lilac)"/>
    </linearGradient>
    <linearGradient id="back-field" x1="0" y1="0" x2="0.3" y2="1">
      <stop offset="0" stop-color="var(--cream)"/>
      <stop offset="0.14" stop-color="var(--olive)"/>
      <stop offset="0.26" stop-color="var(--slate)"/>
      <stop offset="0.36" stop-color="var(--clay)"/>
      <stop offset="0.5" stop-color="var(--periwinkle)"/>
      <stop offset="0.62" stop-color="var(--lemon)"/>
      <stop offset="0.74" stop-color="var(--wheat)"/>
      <stop offset="0.86" stop-color="var(--fern)"/>
      <stop offset="1" stop-color="var(--sage)"/>
    </linearGradient>
  </defs>
  <rect width="2464" height="1502" style="fill:var(--backdrop)"/>

  <g class="cover-front">
    <rect class="page" x="114" y="68" width="1054" height="1372"/>
    <rect class="colour-field-front" x="186" y="68" width="909" height="1372" role="img" aria-label="Abstract mosaic of pastel and autumn colour blocks"/>
    <g class="title-panel">
      <rect class="title-panel-box" x="300" y="488" width="682" height="151"/>
      <text class="script" x="641" y="532" text-anchor="middle">season</text>
      <text class="season-title" x="641" y="575" text-anchor="middle">utomne - hiver 2019</text>
      <text class="tagline" x="641" y="612" text-anchor="middle">Arty feel</text>
    </g>
    <g class="brand">
      <circle class="brand-dot" cx="641" cy="1330" r="18"/>
      <text class="brand-name" x="641" y="1386" text-anchor="middle">LE CARROUSEL MIRANDE</text>
    </g>
  </g>

  <g class="cover-back">
    <rect class="page" x="1292" y="68" width="1054" height="1372"/>
    <rect class="colour-field-back" x="1364" y="68" width="909" height="1372" role="img" aria-label="Abstract mosaic of large pastel and autumn colour blocks"/>
    <text class="website" x="1818" y="572" text-anchor="middle">www.le-carrouselo.com</text>
    <g class="brand">
      <circle class="brand-dot" cx="1818" cy="1330" r="18"/>
      <text class="brand-name" x="1818" y="1386" text-anchor="middle">LE CARROUSEL MIRANDE</text>
    </g>
  </g>
</svg>
</body>
</html>
```